Flyer Design

tallo roofing specialises in roof restorations, terracotta and concrete tiles, roof cleaning, de-mossing, gutter cleaning, bedding and pointing, over 30 years experience, fully qualified and insured, free no obligation quote, servicing Geelong, Ballarat and Melbourne. 10 year warranty on all work, KEEP IT SMART CATCHY AND SIMPLE, BEFORE AND AFTER PHOTOS A MUST, 10 YEAR WARRANTY NEEDS TO STAND OUT

details that must also appear:

Gareth Pellowe (Director)
0417593864
www.talloroofing.com.au

info@talloroofing.com.au

Industry/Entity Type

Concrete

```html
<!DOCTYPE html>
<html lang="en">
<head>
<meta charset="utf-8">
<title>Tallo Roofing Flyer</title>
<link rel="stylesheet" href="https://fonts.googleapis.com/css2?family=Cormorant+Garamond:wght@400;500;600&display=swap">
<style>
  :root {
    --brown: #7a6b5e;
    --text: #7d7168;
    --blue: #00aee8;
    --grey: #d4d0cd;
    --paper: #ffffff;
    --stage: #ffffff;
    --roof-light: #eceae7;
    --roof-mid: #dedad6;
  }
  * { margin: 0; padding: 0; box-sizing: border-box; }
  html, body { width: 1200px; height: 1000px; overflow: hidden; background: var(--stage); }
  body { position: relative; font-family: "Cormorant Garamond", Georgia, serif; color: var(--text); font-variant-numeric: lining-nums; }

  .flyer { position: absolute; background: var(--paper); overflow: hidden; box-shadow: 0 0 0 1px #e6e3e0; }
  .flyer-front { left: 72px; top: 117px; width: 604px; height: 428px; }
  .flyer-back { left: 522px; top: 413px; width: 605px; height: 427px; }

  .waves { position: absolute; left: 0; top: 0; width: 100%; height: 100%; }

  .brand { position: absolute; font-weight: 500; color: var(--brown); letter-spacing: 0.5px; white-space: nowrap; }
  .flyer-front .brand { left: 18px; top: 16px; font-size: 23px; }

  .photo { position: absolute; top: 52px; width: 278px; height: 166px; }
  .photo-before { left: 18px; background: linear-gradient(180deg, #c9d4dc 0%, #b9b49c 20%, #d6c9ad 45%, #8a8d6a 70%, #9c9484 100%); }
  .photo-after { left: 306px; background: linear-gradient(180deg, #c9d4dc 0%, #a3a686 20%, #c87a5c 45%, #7e8c60 70%, #9c9484 100%); }
  .photo-label { position: absolute; bottom: -10px; left: -4px; font-size: 32px; color: #fff; line-height: 1; }

  .services { position: absolute; left: 36px; top: 241px; width: 334px; font-size: 13.5px; line-height: 1.2; letter-spacing: 0.2px; }
  .services .lead { font-size: 19px; }
  .divider { position: absolute; left: 381px; top: 244px; width: 1px; height: 44px; background: var(--brown); }
  .benefits { position: absolute; left: 398px; top: 241px; list-style: none; font-size: 13.5px; line-height: 1.18; }
  .benefits li::before { content: "• "; }

  .contact { position: absolute; left: 0; width: 100%; font-size: 13.5px; letter-spacing: 0.4px; color: var(--text); white-space: nowrap; }
  .contact .sep { display: inline-block; width: 2px; height: 15px; background: var(--brown); vertical-align: middle; margin: 0 5px 0 8px; }
  .flyer-front .contact { top: 393px; left: 136px; }

  .roof-backdrop { position: absolute; left: 0; top: 0; width: 100%; height: 330px; background: linear-gradient(180deg, #f2f1ef 0%, var(--roof-light) 35%, var(--roof-mid) 100%); opacity: 0.9; }
  .flyer-back .brand { left: 0; width: 100%; text-align: center; top: 114px; font-size: 25px; }
  .warranty { position: absolute; left: 135px; top: 172px; font-size: 17px; color: var(--text); white-space: nowrap; }
  .warranty strong { font-size: 27px; font-weight: 500; }
  .coverage { position: absolute; left: 166px; top: 208px; font-size: 19px; white-space: nowrap; }
  .flyer-back .contact { text-align: center; }
  .flyer-back .director { top: 364px; }
  .flyer-back .lines { top: 385px; }
</style>
</head>
<body>

<section class="flyer flyer-front">
  <svg class="waves" viewBox="0 0 604 428" preserveAspectRatio="none" aria-hidden="true">
    <path d="M0,330 C150,345 400,338 604,322 L604,428 L0,428 Z" fill="var(--brown)"/>
    <path d="M0,290 C50,330 150,355 300,360 C420,363 520,350 604,345 L604,428 L0,428 Z" fill="var(--blue)"/>
    <path d="M0,300 C50,338 150,366 300,372 C420,375 520,366 604,362 L604,428 L0,428 Z" fill="var(--grey)"/>
  </svg>

  <div class="brand">Tallo Roofing</div>

  <div class="photo photo-before" role="img" aria-label="Photo of a tiled house roof with solar panels before restoration">
    <span class="photo-label">Before</span>
  </div>
  <div class="photo photo-after" role="img" aria-label="Photo of the same house roof after restoration with fresh red tiles">
    <span class="photo-label">After</span>
  </div>

  <p class="services"><span class="lead">Tallo</span> roofing specializes in roof restorations, terracotta &amp; concrete tiles, roof cleaning, de-mossing, gutter cleaning, bedding and pointing.</p>
  <span class="divider"></span>
  <ul class="benefits">
    <li>Over 30 years experience</li>
    <li>Fully qualified and insured</li>
    <li>Free no obligation quote</li>
  </ul>

  <p class="contact">Director: Gareth Pellowe<span class="sep"></span>info@talloroofing.com.au</p>
</section>

<section class="flyer flyer-back">
  <div class="roof-backdrop" role="img" aria-label="Faded photo of a restored tiled roof with trees behind"></div>
  <svg class="waves" viewBox="0 0 605 427" preserveAspectRatio="none" aria-hidden="true">
    <path d="M0,218 C80,275 250,290 400,295 C500,298 560,300 605,302 L605,427 L0,427 Z" fill="var(--brown)"/>
    <path d="M0,250 C80,300 250,302 400,302 C500,302 560,310 605,322 L605,427 L0,427 Z" fill="var(--blue)"/>
    <path d="M0,280 C100,322 260,320 400,314 C500,310 560,330 605,355 L605,427 L0,427 Z" fill="var(--grey)"/>
  </svg>

  <div class="brand">Tallo Roofing</div>
  <p class="warranty"><strong>10 yr. warranty</strong> on all work</p>
  <p class="coverage">Servicing Geelong, Ballarat and Melbourne.</p>

  <p class="contact director">Director: Gareth Pellowe</p>
  <p class="contact lines">(04) 1759-3864<span class="sep"></span>www.talloroofing.com.au</p>
</section>

</body>
</html>
```